Business card for a boutique travel agency VELARIEN

we need a business card design - double sided. We would like to have a very elegant, sophisticated but modern design. we are travel consultants and our business focus is Europe, mainly the city of Paris. We would like to receive designs in white and silver, black color but if you are confident that we should pick up a color to make it different and more beautful...go ahead! We are going to give business cards to our clients and business partners. It is important to be perceived as elegant, modern and trustful. Please check jpg references.

Target Market(s)

Velarien primary clients are individuals, couples and affinity groups of high-net-worth who travel for leisure at least once per year. Seeking the ultimate travel experience, the target clients demand the finest quality activities and accommodations accompanied by a superior level of service.

Industry/Entity Type

Travel Industry

Contact Information for Business Card

Lucinda Farrow
- lucinda@velarien-example.com
- +55 11 98347.2516
- velarien-example.com
- unique travel experiences (we would like to see this signature printed as a detail)

Font styles to use
Sans Serif

Colors

Designer to choose colors to be used in the design.

Requirements
Must have
• the Velarien logo that I have attached
Nice to have
• we would like to have some nice detail, something different that shows that we care about,... we are detail oriented.
Should not have
• decorative fonts

```html
<!DOCTYPE html>
<html lang="en">
<head>
<meta charset="utf-8">
<title>Velarien — Business Card</title>
<link rel="stylesheet" href="https://fonts.googleapis.com/css2?family=Roboto:wght@300;400;500;700&display=swap">
<style>
  :root {
    --backdrop-light: #eeece8;
    --backdrop-dark: #cfccc7;
    --card-white: #f7f6f4;
    --card-shade: #e6e4e1;
    --copper: #d08a4c;
    --copper-soft: #dba274;
  }
  * { margin: 0; padding: 0; box-sizing: border-box; }
  html, body { width: 1200px; height: 900px; overflow: hidden; }
  body {
    font-family: "Roboto", sans-serif;
    background: radial-gradient(ellipse at 50% 40%, var(--backdrop-light) 0%, var(--backdrop-dark) 100%);
    display: flex;
    flex-direction: column;
    align-items: center;
    justify-content: center;
    gap: 56px;
  }
  .card {
    width: 640px;
    height: 366px;
    background: linear-gradient(160deg, var(--card-white) 0%, var(--card-white) 55%, var(--card-shade) 100%);
    box-shadow: 0 2px 4px rgba(0,0,0,0.18), 0 10px 24px rgba(0,0,0,0.10);
    position: relative;
    color: var(--copper);
  }

  /* Back side: contact details + wordmark */
  .contact {
    position: absolute;
    top: 40px;
    right: 40px;
    text-align: right;
  }
  .contact-name {
    font-weight: 700;
    font-size: 22px;
    letter-spacing: 0.5px;
    text-transform: uppercase;
    margin-bottom: 10px;
  }
  .contact-line {
    display: flex;
    justify-content: flex-end;
    align-items: center;
    gap: 10px;
    font-weight: 400;
    font-size: 15px;
    line-height: 22px;
    color: var(--copper-soft);
  }
  .contact-line svg { width: 13px; height: 13px; fill: var(--copper); }
  .wordmark {
    position: absolute;
    left: 40px;
    right: 40px;
    bottom: 62px;
    text-align: right;
    font-weight: 300;
    font-size: 34px;
    letter-spacing: 16px;
    color: var(--copper-soft);
  }

  /* Front side: brand name + signature line */
  .brand {
    position: absolute;
    top: 118px;
    left: 0;
    right: 0;
    display: flex;
    justify-content: center;
    align-items: center;
    gap: 16px;
  }
  .brand-dot {
    width: 18px;
    height: 18px;
    border-radius: 50%;
    background: var(--copper);
  }
  .brand-name {
    font-weight: 300;
    font-size: 40px;
    letter-spacing: 12px;
    color: var(--copper);
  }
  .signature {
    position: absolute;
    bottom: 70px;
    left: 0;
    right: 0;
    text-align: center;
    font-weight: 500;
    font-size: 17px;
    letter-spacing: 2px;
    color: var(--copper);
  }
</style>
</head>
<body>
  <section class="card card-back" aria-label="Card back">
    <div class="contact">
      <p class="contact-name">Lucinda Farrow</p>
      <p class="contact-line">+55 11 98347.2516
        <svg viewBox="0 0 24 24" aria-hidden="true"><path d="M6.6 10.8c1.4 2.8 3.8 5.1 6.6 6.6l2.2-2.2c.3-.3.7-.4 1-.2 1.1.4 2.3.6 3.6.6.6 0 1 .4 1 1V20c0 .6-.4 1-1 1C10.6 21 3 13.4 3 4c0-.6.4-1 1-1h3.5c.6 0 1 .4 1 1 0 1.3.2 2.5.6 3.6.1.3 0 .7-.2 1L6.6 10.8z"/></svg>
      </p>
      <p class="contact-line">lucinda@velarien-example.com
        <svg viewBox="0 0 24 24" aria-hidden="true"><path d="M2 5h20v14H2z M3 6l9 7 9-7" fill="none" stroke="#d08a4c" stroke-width="2"/></svg>
      </p>
      <p class="contact-line">www.velarien-example.com
        <svg viewBox="0 0 24 24" aria-hidden="true"><circle cx="12" cy="12" r="10"/><path d="M12 2v20M2 12h20" stroke="#f7f6f4" stroke-width="1.5" fill="none"/></svg>
      </p>
    </div>
    <p class="wordmark">VELARIEN</p>
  </section>

  <section class="card card-front" aria-label="Card front">
    <div class="brand">
      <span class="brand-dot"></span>
      <span class="brand-name">VELARIEN</span>
    </div>
    <p class="signature">unique travel experiences</p>
  </section>
</body>
</html>
```